Banner Ad Design Project -

We need banner ads of the following sizes:
250 x 250 square
200 x 200 small square
468 x 60 banner
728 x 90 leaderboard
300 x 250 inline rectangle
336 x 280 large rectangle
120 x 600 skyscraper
160 x 600 wide skyscraper
You can see examples of what we have here: https://www.krelvia.net/banners
These are out of date as our pricing has reduced (the price is now From £2.00)
We need a new, clean look / design in all of the above sizes.

Target Market(s)

You can see the competition's banners here: http://www.tarnwickpost.com/

Requirements
Must have
• Must have our company logo (as attached).

Must have the following text:

Headline:
Great Value UK VPS

Content:
Instant Setup
Moneyback Guarantee
24x7 Support
From £2.00 per month
Nice to have
• Can be animated to grab attention.

```html
<!DOCTYPE html>
<html lang="en">
<head>
<meta charset="utf-8">
<title>Krelvia VPS Banner Set</title>
<link href="https://fonts.googleapis.com/css2?family=Arimo:wght@400;700&family=Oswald:wght@700&display=swap" rel="stylesheet">
<style>
  :root {
    --page: #d9d9d9;
    --navy-deep: #062a5c;
    --navy: #0b3d80;
    --blue: #1565b8;
    --blue-glow: #3d8fe0;
    --white: #ffffff;
    --muted: #b9cbe6;
    --orange-top: #ffd43b;
    --orange-bottom: #f59a0a;
    --ink: #1b1b1b;
    --gold: #e0a823;
    --gold-light: #f7d36a;
    --badge-core: #2a2419;
    --ribbon: #e3161b;
    --server-dark: #1c2632;
    --server-light: #5fb4dd;
  }
  * { box-sizing: border-box; margin: 0; padding: 0; }
  html, body { width: 1200px; height: 1045px; overflow: hidden; }
  body {
    background: var(--page);
    font-family: "Arimo", Arial, sans-serif;
    position: relative;
  }
  .banner {
    position: absolute;
    overflow: hidden;
    color: var(--white);
    background: radial-gradient(ellipse at 50% 70%, var(--blue-glow) 0%, var(--blue) 30%, var(--navy) 65%, var(--navy-deep) 100%);
  }
  .banner > * { position: absolute; }
  .brand {
    font-weight: 700; color: var(--white); line-height: 1; white-space: nowrap;
  }
  .features { list-style: none; text-align: center; font-weight: 400; text-transform: uppercase; }
  .features li { position: absolute; left: 0; right: 0; white-space: nowrap; line-height: 1; }
  .cta {
    background: linear-gradient(var(--orange-top), var(--orange-bottom));
    border: 1px solid #fff3c4;
    color: var(--ink);
    text-align: center; text-transform: uppercase; font-weight: 700;
    display: flex; flex-direction: column; justify-content: center; line-height: 1.05;
  }
  .cta-small, .cta-big { display: block; }
  .price-badge {
    border-radius: 50%;
    background: radial-gradient(circle at 40% 35%, var(--gold-light), var(--gold) 60%, #a8720f);
    display: flex; align-items: center; justify-content: center;
  }
  .price-core {
    width: 74%; height: 74%; border-radius: 50%;
    background: var(--badge-core);
    border: 2px solid var(--gold-light);
    display: flex; flex-direction: column; align-items: center; justify-content: center;
    color: var(--gold-light); font-weight: 700; line-height: 1;
  }
  .price-amount { font-size: 1em; }
  .price-note { font-size: 0.22em; color: var(--white); margin-top: 2px; white-space: nowrap; }
  .price-url { font-size: 0.15em; color: var(--gold-light); margin-top: 2px; white-space: nowrap; }
  .server-art {
    background: linear-gradient(100deg, var(--server-dark) 0%, var(--server-light) 45%, var(--server-dark) 100%);
    border-radius: 3px;
    opacity: 0.9;
  }
  .server-art.cabinet { background: linear-gradient(90deg, #0c0f13, #3a3f46 50%, #111418); }

  /* wide skyscraper */
  .skyscraper { left: 80px; top: 73px; width: 177px; height: 664px; }
  .skyscraper .brand { left: 0; right: 0; top: 24px; text-align: center; font-size: 28px; }
  .skyscraper .headline { left: 0; right: 0; top: 92px; text-align: center; font-weight: 700; font-size: 17px; line-height: 22px; text-transform: uppercase; }
  .skyscraper .headline span { display: block; color: var(--muted); }
  .skyscraper .features { left: 0; right: 0; top: 162px; font-size: 12px; }
  .skyscraper .features li:nth-child(1) { top: 0; }
  .skyscraper .features li:nth-child(2) { top: 30px; }
  .skyscraper .features li:nth-child(3) { top: 59px; }
  .skyscraper .price-badge { left: 43px; top: 254px; width: 90px; height: 90px; font-size: 30px; }
  .skyscraper .server-art { left: 25px; top: 370px; width: 128px; height: 132px; }
  .skyscraper .cta { left: 13px; top: 527px; width: 153px; height: 35px; }
  .skyscraper .cta-small { font-size: 9px; }
  .skyscraper .cta-big { font-size: 14px; }
  .skyscraper .footer-band { left: -30px; right: -30px; top: 590px; bottom: 0; border-radius: 50% 50% 0 0 / 22px 22px 0 0; background: linear-gradient(var(--blue), #0f5fb8); }
  .skyscraper .site { left: 0; right: 0; top: 618px; text-align: center; font-size: 12px; font-weight: 700; color: var(--muted); }

  /* large vertical */
  .tower { left: 372px; top: 73px; width: 332px; height: 664px; }
  .tower .top-arc { left: -40px; right: -40px; top: -60px; height: 160px; border-radius: 0 0 50% 50%; background: linear-gradient(#0a3a78, #0b4186); }
  .tower .brand { left: 0; right: 0; top: 26px; text-align: center; font-size: 34px; }
  .tower .offer-ribbon { right: -34px; top: 14px; width: 130px; height: 20px; background: var(--ribbon); transform: rotate(45deg); color: var(--white); font-size: 10px; font-weight: 700; text-align: center; line-height: 20px; }
  .tower .headline { left: 0; right: 0; top: 114px; text-align: center; font-family: "Oswald", "Arial Narrow", sans-serif; font-size: 31px; text-transform: uppercase; color: #e6eaf0; }
  .tower .features { left: 0; right: 0; top: 190px; font-size: 15px; }
  .tower .features li:nth-child(1) { top: 0; }
  .tower .features li:nth-child(2) { top: 40px; }
  .tower .features li:nth-child(3) { top: 80px; }
  .tower .cta { left: 65px; top: 309px; width: 198px; height: 45px; }
  .tower .cta-small { font-size: 11px; }
  .tower .cta-big { font-size: 18px; }
  .tower .price-badge { left: 108px; top: 386px; width: 116px; height: 116px; font-size: 38px; }
  .tower .server-art { left: 38px; top: 497px; width: 243px; height: 127px; }

  /* rectangle */
  .rectangle { left: 798px; top: 73px; width: 332px; height: 277px; }
  .rectangle .brand { left: 0; right: 0; top: 20px; text-align: center; font-size: 26px; }
  .rectangle .features { left: 0; right: 0; top: 73px; font-size: 12px; }
  .rectangle .features li:nth-child(1) { top: 0; }
  .rectangle .features li:nth-child(2) { top: 29px; }
  .rectangle .features li:nth-child(3) { top: 57px; }
  .rectangle .server-art { left: 65px; top: 159px; width: 205px; height: 97px; }
  .rectangle .price-badge { left: 53px; top: 139px; width: 80px; height: 80px; font-size: 27px; }

  /* leaderboard */
  .leaderboard { left: 70px; top: 831px; width: 806px; height: 100px; background: linear-gradient(110deg, var(--navy-deep) 0%, var(--navy) 28%, var(--blue) 52%, #0a3a78 60%, var(--navy) 100%); }
  .leaderboard .brand { left: 23px; top: 33px; font-size: 32px; }
  .leaderboard .features { left: 233px; top: 24px; font-size: 14px; text-align: left; width: 220px; }
  .leaderboard .features li:nth-child(1) { top: 0; }
  .leaderboard .features li:nth-child(2) { top: 18px; }
  .leaderboard .features li:nth-child(3) { top: 36px; }
  .leaderboard .price-badge { left: 456px; top: 12px; width: 76px; height: 76px; font-size: 26px; }
  .leaderboard .server-art { left: 578px; top: 4px; width: 182px; height: 92px; }
</style>
</head>
<body>

<section class="banner skyscraper" aria-label="Krelvia wide skyscraper banner">
  <div class="brand">Krelvia</div>
  <h2 class="headline">Great Value<span>UK VPS</span></h2>
  <ul class="features"><li>Instant Setup</li><li>Moneyback Guarantee</li><li>24X7 Support</li></ul>
  <div class="price-badge"><div class="price-core"><span class="price-amount">2£</span><span class="price-note">from per month</span><span class="price-url">www.krelvia.net</span></div></div>
  <div class="server-art cabinet" role="img" aria-label="Black server cabinet illustration"></div>
  <div class="footer-band"></div>
  <a class="cta"><span class="cta-small">For more information</span><span class="cta-big">Click here</span></a>
  <div class="site">WWW.KRELVIA.NET</div>
</section>

<section class="banner tower" aria-label="Krelvia large vertical banner">
  <div class="top-arc"></div>
  <div class="brand">Krelvia</div>
  <div class="offer-ribbon">50 %OFF</div>
  <h2 class="headline">Great Value UK VPS</h2>
  <ul class="features"><li>Instant Setup</li><li>Moneyback Guarantee</li><li>24X7 Support</li></ul>
  <a class="cta"><span class="cta-small">For more information</span><span class="cta-big">Click here</span></a>
  <div class="server-art" role="img" aria-label="Row of blue server towers in perspective"></div>
  <div class="price-badge"><div class="price-core"><span class="price-amount">2£</span><span class="price-note">from per month</span><span class="price-url">www.krelvia.net</span></div></div>
</section>

<section class="banner rectangle" aria-label="Krelvia rectangle banner">
  <div class="brand">Krelvia</div>
  <ul class="features"><li>Instant Setup</li><li>Moneyback Guarantee</li><li>24X7 Support</li></ul>
  <div class="server-art" role="img" aria-label="Row of blue server towers in perspective"></div>
  <div class="price-badge"><div class="price-core"><span class="price-amount">2£</span><span class="price-note">from per month</span><span class="price-url">www.krelvia.net</span></div></div>
</section>

<section class="banner leaderboard" aria-label="Krelvia leaderboard banner">
  <div class="brand">Krelvia</div>
  <ul class="features"><li>Instant Setup</li><li>Moneyback Guarantee</li><li>24X7 Support</li></ul>
  <div class="price-badge"><div class="price-core"><span class="price-amount">2£</span><span class="price-note">from per month</span><span class="price-url">www.krelvia.net</span></div></div>
  <div class="server-art" role="img" aria-label="Row of blue server towers in perspective"></div>
</section>

</body>
</html>
```